Chinese Language Posters - KNHLY

We have created a series of African American heritage posters that will be distributed to Chinese Language Schools. We need a designer to create great posters for K-12 programs.

Quotes:
We have quotes from 6 important figures in Black History. We are seeking a designer to develop a poster utilizing at least one quote from each historical figure.

The designer MUST be fluent in Chinese in order to ensure the appropriate type and font.

Our organization, Kinfolk Network for Heritage Language Youth Mentoring, is a small organization of parents in the Bay Area working to encourage and support Black students learning the Chinese language.

Target Market(s)

These posters will be made available to Chinese Immersion schools (k-12).

Industry/Entity Type

Learning

Requirements
Must have
• Each poster should contain one quote from the list below.

Please create a poster of one historical figure and include their quote. The image can be abstract, landscape or an image of the figure.

The image should also include our logo. Our preferred logo is with the puffs but we understand if the clipart logo may be a better fit for the posters. (We LOVE the puffs logo though).
Nice to have
• I have uploaded images of each figure. The images can be used or a more abstract background. We are flexible. We would prefer a mix that includes figures and abstract backgrounds just focusing on the quote. We are open.

```html
<!DOCTYPE html>
<html lang="zh-Hans">
<head>
<meta charset="utf-8">
<title>没有斗争，就没有进步 — KNHLY</title>
<link rel="stylesheet" href="https://fonts.googleapis.com/css2?family=Noto+Sans+SC:wght@500&family=Roboto+Condensed:wght@400&display=swap">
<style>
  :root {
    --poster-orange: #d47a55;
    --map-mint: #eef7e2;
    --portrait-cream: #e9e2d6;
    --ink: #2b2421;
    --logo-cream: #f6ecd4;
  }
  html, body {
    margin: 0;
    padding: 0;
    overflow: hidden;
  }
  body {
    width: 848px;
    height: 1200px;
  }
  .poster {
    position: relative;
    width: 848px;
    height: 1200px;
    background: var(--poster-orange);
    overflow: hidden;
  }
  .flag-map {
    position: absolute;
    left: 40px;
    top: 80px;
    width: 808px;
    height: 375px;
    background: linear-gradient(180deg, var(--map-mint) 0%, rgba(238, 247, 226, 0.55) 100%);
    opacity: 0.55;
  }
  .portrait {
    position: absolute;
    left: 240px;
    top: 225px;
    width: 460px;
    height: 975px;
    border-radius: 200px 200px 0 0;
    background: linear-gradient(180deg, var(--portrait-cream) 0%, rgba(233, 226, 214, 0.6) 45%, rgba(233, 226, 214, 0) 100%);
    opacity: 0.7;
  }
  .quote-block {
    position: absolute;
    left: 83px;
    top: 700px;
    color: var(--ink);
    font-family: "Noto Sans SC", sans-serif;
    font-weight: 500;
  }
  .quote {
    margin: 0;
    font-size: 46px;
    line-height: 1.2;
    letter-spacing: 0.02em;
  }
  .attribution {
    margin: 22px 0 0;
    font-size: 64px;
    line-height: 1.2;
    letter-spacing: 0.04em;
  }
  .org-mark {
    position: absolute;
    right: 10px;
    bottom: 14px;
    width: 150px;
    display: flex;
    flex-direction: column;
    align-items: center;
    color: var(--logo-cream);
    font-family: "Roboto Condensed", sans-serif;
    font-weight: 400;
  }
  .org-dot {
    width: 64px;
    height: 64px;
    border-radius: 50%;
    background: var(--logo-cream);
    margin-bottom: 10px;
  }
  .org-name {
    font-size: 40px;
    line-height: 1;
    letter-spacing: 0.02em;
  }
  .org-tagline {
    margin-top: 4px;
    font-size: 6.5px;
    line-height: 1.2;
    text-align: center;
    white-space: nowrap;
  }
</style>
</head>
<body>
  <main class="poster">
    <div class="flag-map" role="img" aria-label="Map of the United States filled with the stars and stripes of the flag"></div>
    <div class="portrait" role="img" aria-label="Posterised portrait of the historical figure with white hair and beard"></div>

    <section class="quote-block">
      <p class="quote">没有斗争，就没有进步。</p>
      <p class="attribution">塞缪尔·哈德威克</p>
    </section>

    <div class="org-mark">
      <span class="org-dot"></span>
      <span class="org-name">KNHLY</span>
      <span class="org-tagline">Kinfolk Network for Heritage Language Youth Mentoring</span>
    </div>
  </main>
</body>
</html>
```